Todo-list with focus on focus

We are writing todo app which is a to-do list/ outliner with focus support based on pomodoro method.

Attached are very rough mockups, but they are conceptually correct.

Main idea behind an app - minimum (unneeded) functionality and maximum benefit to the user.

So, everything must be very intuitive, fast, and without distractions (let's say Quince-style)

Target Market(s)

People who want to spend less time organizing their todo list than using it

Industry/Entity Type

It Support

Requirements
Must have
• Everything which is in mockups, maybe you can drop 1 or 2 if absolutely needed.
Nice to have
• 1. We would like to see such pallete here: http://www.huebinder.example/palette/482706/Mossy_Harbor_Dusk but it's not mandatory.
If you propose some other pallete, please make sure it's beautiful.

2. It would be good to somehow indicate that project is a goal in project list, and task is a goal in goal's list

3. Inbox should be accessible easliy, probably by sticking it to the top of Projects list somehow.

4. If you are able to propose another way to deal with such amount of options to deal with tasks other than radial menu - you are free to do it, if it'll work.

5. Priority, tags - very nice to have if they will fit into conception.

6. Maybe you can add other stuff we have overlooked.
But, if added, it must be very simple and needed.

```html
<!DOCTYPE html>
<html lang="en">
<head>
<meta charset="utf-8">
<title>Focus – todo outliner</title>
<link rel="stylesheet" href="https://fonts.googleapis.com/css2?family=Arimo:wght@400;700&display=swap">
<style>
  :root {
    --page: #edecf0;
    --ink-black: #000000;
    --panel-dark: #222222;
    --panel-darker: #1c1c1c;
    --divider: #111111;
    --text-light: #f4f4f4;
    --text-muted: #c9c9c9;
    --brown: #5b3f2e;
    --brown-light: #7a5a45;
    --cream: #f3e3b2;
    --cream-pale: #fbf3dc;
    --teal: #6fb59e;
    --orange: #e0741c;
    --amber: #efa836;
    --amber-light: #f6c15a;
    --red: #c4080b;
    --card: #fdfbf5;
    --card-line: #d9d3c4;
    --card-text: #6a655c;
  }
  * { box-sizing: border-box; margin: 0; padding: 0; }
  html, body { width: 756px; height: 1200px; overflow: hidden; }
  body { background: var(--page); font-family: "Arimo", Arial, sans-serif; position: relative; }

  .screen { position: absolute; left: 58px; top: 32px; width: 640px; height: 1136px; overflow: hidden; background: var(--panel-dark); }

  .status-bar { position: absolute; left: 0; top: 0; width: 640px; height: 46px; background: var(--ink-black); color: var(--text-light); font-size: 24px; font-weight: 700; }
  .status-bar .carrier { position: absolute; left: 12px; top: 9px; display: flex; align-items: center; gap: 8px; }
  .status-bar .signal { display: flex; align-items: flex-end; gap: 2px; height: 16px; }
  .status-bar .signal i { display: block; width: 4px; background: var(--text-light); }
  .status-bar .clock { position: absolute; left: 0; width: 640px; top: 9px; text-align: center; }
  .status-bar .battery { position: absolute; right: 14px; top: 13px; width: 38px; height: 18px; border: 2px solid var(--text-light); border-radius: 3px; padding: 2px; }
  .status-bar .battery::before { content: ""; display: block; height: 100%; background: var(--text-light); }
  .status-bar .alarm { position: absolute; right: 64px; top: 14px; width: 16px; height: 16px; border-radius: 50%; background: var(--text-light); }

  .focus-panel { position: absolute; left: 0; top: 46px; width: 514px; height: 1090px; background: var(--panel-dark); }
  .focus-header { height: 90px; background: linear-gradient(#6a6a6a, #3c3c3c); border-bottom: 2px solid var(--divider); color: var(--text-light); font-size: 40px; padding: 18px 0 0 16px; letter-spacing: .3px; }

  .current-task { position: relative; height: 390px; }
  .task-title { position: absolute; left: 20px; top: 26px; font-size: 37px; font-weight: 700; color: var(--text-light); }
  .progress-row { position: absolute; left: 20px; font-size: 26px; color: var(--text-muted); }
  .progress-row.completed { top: 84px; }
  .progress-row.left { top: 132px; }
  .dots { position: absolute; left: 152px; top: 4px; display: flex; gap: 8px; }
  .dot { width: 18px; height: 18px; border-radius: 50%; border: 2px solid var(--teal); }
  .dot.done { background: var(--teal); }
  .stepper { position: absolute; left: 392px; top: 100px; width: 102px; height: 50px; border-radius: 8px; background: linear-gradient(#8fd0bb, var(--teal)); display: flex; box-shadow: inset 0 1px 0 rgba(255,255,255,.5); }
  .stepper span { flex: 1; display: flex; align-items: center; justify-content: center; }
  .stepper span + span { border-left: 2px solid rgba(255,255,255,.6); }

  .timer { position: absolute; left: 20px; top: 188px; width: 474px; height: 170px; border-radius: 8px; background: linear-gradient(var(--amber-light), var(--amber) 60%, #e89424); border: 2px solid #b8741c; }
  .timer-label { position: absolute; left: 16px; top: 14px; font-size: 40px; color: #3a2510; }
  .timer-value { position: absolute; left: 42px; top: 60px; font-size: 88px; font-weight: 700; color: #fff; letter-spacing: -1px; text-shadow: 0 2px 2px rgba(0,0,0,.35); }
  .stop-button { position: absolute; left: 300px; top: 86px; width: 154px; height: 54px; border-radius: 8px; background: linear-gradient(#e0282a, var(--red) 55%, #9b0406); border: 2px solid #6d0000; color: #fff; font-size: 30px; font-weight: 700; display: flex; align-items: center; justify-content: center; }

  .goal-section-title { height: 62px; background: linear-gradient(var(--brown-light), var(--brown)); border-top: 2px solid var(--divider); border-bottom: 2px solid var(--divider); color: var(--text-light); font-size: 30px; padding: 14px 0 0 18px; }
  .goal-list { list-style: none; padding: 8px 0 14px; }
  .goal-item { height: 60px; display: flex; align-items: center; padding-left: 18px; font-size: 28px; color: var(--text-muted); }
  .checkbox { width: 38px; height: 38px; border-radius: 7px; background: var(--cream); border: 2px solid #c9ad6e; margin-right: 20px; display: flex; align-items: center; justify-content: center; }
  .checkbox.checked { background: var(--orange); border-color: #b0540c; }

  .project-panel { position: absolute; left: 514px; top: 46px; width: 400px; height: 1090px; background: var(--cream-pale); box-shadow: -6px 0 10px rgba(0,0,0,.5); }
  .project-toolbar { height: 90px; background: linear-gradient(#f0a248, var(--orange)); border-bottom: 2px solid #9a4e10; }
  .alert-button { position: absolute; left: 16px; top: 12px; width: 84px; height: 66px; border-radius: 8px; background: linear-gradient(#f7b26a, var(--orange)); border: 2px solid #a64f0c; display: flex; align-items: center; justify-content: center; }
  .new-task-box { position: absolute; left: 16px; top: 108px; width: 300px; height: 172px; border-radius: 8px; background: linear-gradient(#7c5d4a, var(--brown)); border: 2px solid #3e2a1e; }
  .new-task-input { position: absolute; left: 22px; top: 94px; width: 280px; height: 56px; border-radius: 10px; background: #fff; border: 2px solid #3e2a1e; font-size: 24px; color: #8a8a8a; padding: 14px 0 0 16px; white-space: nowrap; }
  .task-card { position: absolute; left: 16px; top: 300px; width: 300px; height: 800px; background: var(--card); border: 2px solid var(--card-line); border-radius: 6px 0 0 0; color: var(--card-text); font-size: 28px; }
  .task-row { position: absolute; left: 20px; white-space: nowrap; }
  .sub-row { position: absolute; white-space: nowrap; font-size: 26px; padding-left: 18px; border-left: 2px solid #9a9387; height: 40px; line-height: 40px; }
  .sub-row.boxed { border: 2px solid #e0cfa0; background: #fffbee; height: 38px; line-height: 34px; padding-left: 12px; }
  .card-divider { position: absolute; left: 0; width: 300px; border-top: 2px solid var(--card-line); }
</style>
</head>
<body>
  <div class="screen">
    <div class="status-bar">
      <div class="carrier">
        <span class="signal"><i style="height:5px"></i><i style="height:8px"></i><i style="height:11px"></i><i style="height:14px"></i><i style="height:16px"></i></span>
        <span>KESTREL&nbsp;&nbsp;3G</span>
      </div>
      <div class="clock">4:20 AM</div>
      <span class="alarm"></span>
      <span class="battery"></span>
    </div>

    <section class="focus-panel">
      <h1 class="focus-header" style="font-weight:400">I am focused on...</h1>

      <div class="current-task">
        <h2 class="task-title">Task 1</h2>
        <div class="progress-row completed">Completed<span class="dots"><span class="dot done"></span></span></div>
        <div class="progress-row left">Left<span class="dots"><span class="dot"></span><span class="dot"></span></span></div>
        <div class="stepper">
          <span><svg width="26" height="26" viewBox="0 0 26 26"><rect x="2" y="10" width="22" height="6" fill="#fff"/></svg></span>
          <span><svg width="26" height="26" viewBox="0 0 26 26"><rect x="2" y="10" width="22" height="6" fill="#fff"/><rect x="10" y="2" width="6" height="22" fill="#fff"/></svg></span>
        </div>
        <div class="timer">
          <div class="timer-label">Time Left</div>
          <div class="timer-value">21:34</div>
          <div class="stop-button">Stop</div>
        </div>
      </div>

      <h3 class="goal-section-title" style="font-weight:400">Daily goals</h3>
      <ul class="goal-list">
        <li class="goal-item"><span class="checkbox"></span>Daily goal 1</li>
        <li class="goal-item"><span class="checkbox"></span>Daily goal 2</li>
        <li class="goal-item"><span class="checkbox checked"><svg width="28" height="28" viewBox="0 0 28 28"><path d="M4 15 L11 22 L24 6" fill="none" stroke="#fff" stroke-width="4.5" stroke-linecap="round" stroke-linejoin="round"/></svg></span>Daily goal 2</li>
      </ul>

      <h3 class="goal-section-title" style="font-weight:400">Weekly goals</h3>
      <ul class="goal-list">
        <li class="goal-item"><span class="checkbox"></span>Weekly goal 1</li>
        <li class="goal-item"><span class="checkbox"></span>Weekly goal 2</li>
      </ul>

      <h3 class="goal-section-title" style="font-weight:400">Life goals</h3>
      <ul class="goal-list">
        <li class="goal-item"><span class="checkbox"></span>Life goal 1</li>
      </ul>
    </section>

    <section class="project-panel">
      <div class="project-toolbar">
        <div class="alert-button">
          <svg width="50" height="50" viewBox="0 0 50 50"><circle cx="25" cy="25" r="23" fill="#fff"/><rect x="21.5" y="10" width="7" height="20" rx="2" fill="var(--orange)"/><circle cx="25" cy="37" r="4" fill="var(--orange)"/></svg>
        </div>
      </div>
      <div class="new-task-box">
        <div class="new-task-input">Type new task</div>
      </div>
      <div class="task-card">
        <div class="task-row" style="top:24px">Task 1</div>
        <div class="sub-row" style="left:42px;top:78px">Subtask</div>
        <div class="sub-row" style="left:42px;top:128px">Subtask</div>
        <div class="sub-row" style="left:62px;top:178px">Subtask</div>
        <div class="card-divider" style="top:246px"></div>
        <div class="task-row" style="top:272px">Task 2</div>
        <div class="sub-row boxed" style="left:40px;top:330px">Subtask</div>
        <div class="card-divider" style="top:398px"></div>
        <div class="task-row" style="top:422px">Task 3</div>
        <div class="card-divider" style="top:478px"></div>
        <div class="task-row" style="top:502px">Task 4</div>
        <div class="card-divider" style="top:558px"></div>
        <div class="task-row" style="top:582px">Task 5</div>
        <div class="sub-row" style="left:42px;top:638px">Subtask</div>
        <div class="sub-row" style="left:42px;top:688px">Subtask</div>
        <div class="sub-row" style="left:42px;top:738px">Subtask</div>
      </div>
    </section>
  </div>
</body>
</html>
```